We have developed a fully functional App called Corvalink. However, it requires a nicer GUI. You can see screenshots of our App on www.corvalink-example.com under "Tutorial". For those of you with Android, you can also install it. When you go to Corvalink-example.com, your phone will automatically redirect you to download. From there, you'll get a better idea of what our App looks like and how your design can make it way better. Please note we expect a design idea for most screens (there's about 8 screens) but do just one screen first and if you win, you can do the other 8 after.

Target Market(s)

People looking for dating / flirting

Industry/Entity Type

Android

Requirements
Must have
• sleek looking

```html
<!DOCTYPE html>
<html lang="en">
<head>
<meta charset="utf-8">
<title>Corvalink – Home</title>
<link href="https://fonts.googleapis.com/css2?family=Roboto:wght@400;500&display=swap" rel="stylesheet">
<style>
  :root{
    --bar:#000;
    --bg-top:#b87d9f;
    --bg-mid:#9a5f8f;
    --bg-bottom:#5d4389;
    --row-hi:rgba(255,200,220,.28);
    --line:rgba(255,255,255,.35);
    --text:#ffffff;
    --muted:rgba(255,255,255,.88);
    --online:#1fa84a;
    --away:#f0a21b;
    --busy:#d8262b;
    --heart:#e0389a;
    --logo-dot:#4fb4e6;
  }
  *{box-sizing:border-box;margin:0;padding:0}
  html,body{width:675px;height:1200px;overflow:hidden}
  body{font-family:"Roboto",Helvetica,Arial,sans-serif;color:var(--text);
    background:linear-gradient(160deg,var(--bg-top) 0%,var(--bg-mid) 45%,var(--bg-bottom) 100%);position:relative}
  .status-bar{height:40px;background:var(--bar);display:flex;justify-content:flex-end;align-items:center;gap:10px;padding-right:12px;font-size:26px}
  .status-bar svg{display:block}
  .app-header{height:100px;position:relative}
  .brand{position:absolute;left:18px;top:28px;display:flex;align-items:center;gap:14px}
  .brand-dot{width:56px;height:56px;border-radius:50%;background:var(--logo-dot)}
  .brand-name{font-size:40px;font-weight:500;color:var(--text)}
  .header-actions{position:absolute;right:18px;top:34px;display:flex;gap:26px}
  .tabs{height:73px;display:flex;align-items:center;position:relative;font-size:28px;letter-spacing:.5px;border-bottom:1px solid var(--line)}
  .tab{display:flex;align-items:center;gap:10px;justify-content:center;height:100%;position:relative}
  .tab-home{width:184px;font-weight:500}
  .tab-home::after{content:"";position:absolute;left:0;right:0;bottom:-1px;height:4px;background:#fff}
  .tab-sep{width:2px;height:28px;background:rgba(255,255,255,.8)}
  .tab-messages{width:258px;color:var(--muted)}
  .tab-settings{flex:1;color:var(--muted)}
  .profile{height:178px;position:relative;border-bottom:1px solid var(--line)}
  .profile.highlight{background:var(--row-hi)}
  .avatar{position:absolute;left:20px;top:12px;width:152px;height:152px;border-radius:50%;border:3px solid rgba(255,255,255,.9)}
  .presence{position:absolute;left:128px;top:120px;width:34px;height:34px;border-radius:50%;border:3px solid #fff}
  .presence.online{background:var(--online)}
  .presence.away{background:var(--away)}
  .presence.busy{background:var(--busy)}
  .fav{position:absolute;left:24px;top:12px}
  .name{position:absolute;left:194px;top:18px;font-size:31px;font-weight:500;display:flex;align-items:center;gap:12px}
  .name .age{font-size:28px;border-left:1px solid rgba(255,255,255,.7);padding-left:10px}
  .tagline{position:absolute;left:196px;top:64px;width:410px;display:flex;gap:14px;font-size:25px;line-height:1.1}
  .tagline svg{flex:none;margin-top:4px}
  .location{position:absolute;left:196px;top:128px;display:flex;align-items:center;gap:16px;font-size:23px;color:var(--muted)}
  .chevron{position:absolute;right:18px;top:70px}
</style>
</head>
<body>
  <div class="status-bar">
    <svg width="36" height="26" viewBox="0 0 36 26"><path d="M18 24 2 8a23 23 0 0 1 32 0Z" fill="#fff"/></svg>
    <svg width="22" height="26" viewBox="0 0 22 26"><path d="M22 0v26H0Z" fill="#fff"/></svg>
    <svg width="16" height="26" viewBox="0 0 16 26"><rect x="4" y="0" width="8" height="3" fill="#fff"/><rect x="0" y="3" width="16" height="23" fill="#fff"/></svg>
    <span>12:00</span>
  </div>

  <header class="app-header">
    <div class="brand"><span class="brand-dot"></span><span class="brand-name">Corvalink</span></div>
    <div class="header-actions">
      <svg width="46" height="46" viewBox="0 0 46 46" fill="none" stroke="#fff" stroke-width="3"><circle cx="19" cy="19" r="16"/><path d="M31 31 44 44"/></svg>
      <svg width="42" height="46" viewBox="0 0 42 46" fill="none" stroke="#fff" stroke-width="3"><path d="M34 14A18 18 0 1 0 39 28"/><path d="M26 4 35 14 24 18" stroke-linejoin="round"/></svg>
    </div>
  </header>

  <nav class="tabs">
    <div class="tab tab-home">
      <svg width="24" height="24" viewBox="0 0 24 24" fill="#fff"><path d="M12 1 0 12h3v11h7v-7h4v7h7V12h3Z"/></svg>HOME
    </div>
    <span class="tab-sep"></span>
    <div class="tab tab-messages">
      <svg width="28" height="26" viewBox="0 0 28 26" fill="none" stroke="#fff" stroke-width="2"><rect x="1" y="1" width="17" height="13"/><path d="M8 14v10l5-5h14V7h-9"/></svg>MESSAGES
    </div>
    <span class="tab-sep"></span>
    <div class="tab tab-settings">
      <svg width="26" height="26" viewBox="0 0 26 26" fill="none" stroke="#fff" stroke-width="2"><circle cx="13" cy="13" r="4"/><circle cx="13" cy="13" r="9" stroke-dasharray="4 3" stroke-width="5"/></svg>SETTINGS
    </div>
  </nav>

  <svg width="0" height="0" style="position:absolute">
    <defs>
      <symbol id="i-chat" viewBox="0 0 28 24"><path d="M1 1h26v16H10l-5 5v-5H1Z" fill="none" stroke="#fff" stroke-width="2"/><g fill="#fff"><circle cx="9" cy="9" r="1.4"/><circle cx="14" cy="9" r="1.4"/><circle cx="19" cy="9" r="1.4"/></g></symbol>
      <symbol id="i-pin" viewBox="0 0 22 30"><path d="M11 29C4 19 1 15 1 10a10 10 0 0 1 20 0c0 5-3 9-10 19Z" fill="none" stroke="#fff" stroke-width="2"/><circle cx="11" cy="10" r="3.5" fill="none" stroke="#fff" stroke-width="2"/></symbol>
      <symbol id="i-chev" viewBox="0 0 22 40"><path d="M2 2l18 18L2 38" fill="none" stroke="#fff" stroke-width="2.5"/></symbol>
    </defs>
  </svg>

  <main class="profile-list">
    <article class="profile highlight">
      <div class="avatar" role="img" aria-label="Profile photo of Larissa" style="background:linear-gradient(160deg,#d9b07a,#8f7a55)"></div>
      <span class="presence online"></span>
      <h2 class="name">Sensual Larissa <span class="age">♀25</span></h2>
      <p class="tagline"><svg width="28" height="24"><use href="#i-chat"/></svg>Smart, Kind and Drama Free!</p>
      <p class="location"><svg width="22" height="30"><use href="#i-pin"/></svg>Sacremento, USA</p>
      <svg class="chevron" width="22" height="40"><use href="#i-chev"/></svg>
    </article>

    <article class="profile">
      <div class="avatar" role="img" aria-label="Profile photo of Sweetguy85" style="background:linear-gradient(160deg,#6a5a55,#c2302f)"></div>
      <span class="presence online"></span>
      <h2 class="name">Sweetguy85 <span class="age">♂29</span></h2>
      <p class="tagline"><svg width="28" height="24"><use href="#i-chat"/></svg>Sweet, never sour!</p>
      <p class="location"><svg width="22" height="30"><use href="#i-pin"/></svg>New York, USA</p>
      <svg class="chevron" width="22" height="40"><use href="#i-chev"/></svg>
    </article>

    <article class="profile">
      <div class="avatar" role="img" aria-label="Profile photo of Eric" style="background:linear-gradient(160deg,#d8ccc0,#5a3e9a)"></div>
      <span class="presence away"></span>
      <h2 class="name">Zephyr Eric <span class="age">♂23</span></h2>
      <p class="tagline"><svg width="28" height="24"><use href="#i-chat"/></svg>Handsome young talent lives here!</p>
      <p class="location"><svg width="22" height="30"><use href="#i-pin"/></svg>Chigago, USA</p>
      <svg class="chevron" width="22" height="40"><use href="#i-chev"/></svg>
    </article>

    <article class="profile">
      <div class="avatar" role="img" aria-label="Profile photo of Bob" style="background:linear-gradient(160deg,#e4e2e0,#8d96a3)"></div>
      <svg class="fav" width="40" height="36" viewBox="0 0 40 36"><path d="M20 34 4 18A10 10 0 0 1 20 5a10 10 0 0 1 16 13Z" fill="var(--heart)" stroke="#fff" stroke-width="2.5"/></svg>
      <span class="presence busy"></span>
      <h2 class="name">Bob kto <span class="age">♂31</span></h2>
      <p class="tagline"><svg width="28" height="24"><use href="#i-chat"/></svg>Gentle voice and warm heart!</p>
      <p class="location"><svg width="22" height="30"><use href="#i-pin"/></svg>Vancouver, Canada</p>
      <svg class="chevron" width="22" height="40"><use href="#i-chev"/></svg>
    </article>

    <article class="profile">
      <div class="avatar" role="img" aria-label="Profile photo of David" style="background:linear-gradient(160deg,#9aa3a8,#2d3340)"></div>
      <span class="presence online"></span>
      <h2 class="name">David <span class="age">♂39</span></h2>
      <p class="tagline"><svg width="28" height="24"><use href="#i-chat"/></svg>Looking for Pleasure Island? U found it!</p>
      <p class="location"><svg width="22" height="30"><use href="#i-pin"/></svg>Seattle, USA</p>
      <svg class="chevron" width="22" height="40"><use href="#i-chev"/></svg>
    </article>

    <article class="profile">
      <div class="avatar" role="img" aria-label="Profile photo of John" style="background:linear-gradient(180deg,#6f9bc8,#6b5a4a)"></div>
      <h2 class="name">John VL <span class="age">♂35</span></h2>
      <p class="tagline"><svg width="28" height="24"><use href="#i-chat"/></svg>Brave heart, brave love!</p>
      <svg class="chevron" width="22" height="40"><use href="#i-chev"/></svg>
    </article>
  </main>
</body>
</html>
```